Our company TrulaPay, an online processor of payments is seeking talented submissions for our website redesign. The winning design will be chopped up and converted into a WordPress theme to allow for easy content additions and updates.

We are looking for modern designs that rival current websites in our industry (plimo.example, zanquetto.example, holvix.example, brandle.example, quillmarkcharges.example, evensplitcharges.example, KoboRun.example).

Our company is seeking to expand our reach to software developers and engineers who are either integrating our payment platform into their offerings or are engineering a custom solution for the company they work for and are in need of a payment platform such as our own.

We currently work with hundreds of different business partners whom either resell our services or integrate our processing capabilities into their software (which they sell). We also must communicate effectively to end users, businesses, who seek us out directly for their payment processing needs.

We are open to different color schemes but would ultimately like them to be somewhat inline with our current logo (see attached). Our website needs to instill security and confidence to any current and/or potential user as we are trusted with private and sensitive information.

We are seeking submissions from qualified; individual freelancers, freelance teams, and agencies who can attack this project in its entirety. Since this project is a total redesign, we would like submissions that have the capability to design any custom graphics, icons, buttons, and illustrations in line with our industry, capabilities, offerings, and content. We are looking for someone to design our new website and would prefer a vendor who can also help us to design elements (graphics, illustrations, charts, workflows) within our website.

Designs will be converted into a wordpress theme and we would like to utilize widgets for as many areas as possible to make editing and updating easy.

We are seeking the creation of a few unique pages but many of the pages for the majority of our content will just be internal content pages which will be duplicated.

We will likely contract with the winning submission for future work.

Please see Design Reference Document for more information

Target Market(s)

Resellers
Merchant Service Providers
Software Developers
Independent Sales Organizations (ISOs)
App Builders
Mobile App Builders
Independent Software Developers
Organizational Software Developers
Businesses who need to accept payments
Governments
Municipalities
Schools
DMVs
Courts
Retailers
Medical Offices
Hosipitals
Clinics
Dr. Offices
Gyms
Churches
Non-Profits
Software Companies
Technology Companies
Startups

• Logo cannot change drastically.

```html
<!DOCTYPE html>
<html lang="en">
<head>
<meta charset="utf-8">
<title>TrulaPay — Payment Processing</title>
<link rel="stylesheet" href="https://fonts.googleapis.com/css2?family=Roboto:wght@300;400;500;700&display=swap">
<style>
:root{
  --brand-blue:#0a0aa6;
  --brand-red:#e0101a;
  --ink:#3f3f3f;
  --muted:#a9a9a9;
  --nav:#555;
  --band-a:#ffffff;
  --band-b:#ececec;
  --footer:#2f2f2f;
  --footer-text:#9a9a9a;
}
*{margin:0;padding:0;box-sizing:border-box}
html,body{width:1200px;height:3822px;overflow:hidden}
body{font-family:"Roboto",Arial,sans-serif;color:var(--ink);background:#fff;position:relative}
.abs{position:absolute}

/* header */
.site-header{left:0;top:0;width:1200px;height:52px;background:#fff}
.brand{left:120px;top:12px;display:flex;align-items:center;gap:8px;font-size:24px;font-weight:500;color:var(--brand-blue)}
.brand-dot{width:10px;height:10px;border-radius:50%;background:var(--brand-red)}
.main-nav{left:280px;top:20px;display:flex;gap:22px;font-size:12px;color:var(--nav)}
.call{left:757px;top:15px;font-size:16px;color:#777;display:flex;align-items:center;gap:6px}
.call strong{color:#333;font-weight:400}
.btn{top:14px;height:24px;font-size:12px;color:#fff;display:flex;align-items:center;justify-content:center;gap:5px;border-radius:2px}
.btn-email{left:922px;width:88px;background:var(--brand-blue)}
.btn-login{left:1014px;width:62px;background:var(--brand-red)}

/* hero */
.hero{left:0;top:52px;width:1200px;height:343px;background:linear-gradient(100deg,#8e9dc4 0%,#b7c3de 35%,#c8d1e6 55%,#7f8fb9 100%)}
.hero h1{position:absolute;left:0;top:98px;width:1200px;text-align:center;color:#fff;font-weight:300;font-size:48px;line-height:56px;letter-spacing:.5px}

/* feature bands */
.feature{left:0;width:1200px;height:380px}
.feature.light{background:linear-gradient(#fff,#f3f3f3)}
.feature.grey{background:linear-gradient(#e6e6e6,#f7f7f7)}
.feature h2{position:absolute;font-size:26px;font-weight:400;color:#4a4a4a;text-transform:uppercase}
.feature p{position:absolute;width:490px;font-size:12px;line-height:15px;color:var(--muted)}
.feature .art{position:absolute;border-radius:6px}

/* website payment form */
.payform{left:0;top:1911px;width:1200px;height:382px;background:var(--brand-blue);color:#fff}
.payform h2{position:absolute;left:120px;top:88px;font-size:26px;font-weight:500;text-transform:uppercase}
.payform .lead{position:absolute;left:120px;top:126px;width:960px;font-size:12px;line-height:15px}
.payform .item{position:absolute;top:216px;width:310px;display:flex;gap:10px}
.payform .item .thumb{width:115px;height:75px;flex:none}
.payform .item h3{font-size:14px;font-weight:500;margin-bottom:3px}
.payform .item p{font-size:11px;line-height:13px}
.payform .rule{position:absolute;top:216px;width:1px;height:75px;background:rgba(255,255,255,.35)}

/* ACH */
.ach{left:0;top:3430px;width:1200px;height:303px;background:#fff}
.ach h2{position:absolute;left:0;top:18px;width:1200px;text-align:center;font-size:26px;font-weight:400;color:#222}
.ach h2 span{color:var(--brand-red)}
.ach .rule{position:absolute;left:120px;top:66px;width:960px;height:1px;background:#e3e3e3}
.ach .col{position:absolute;top:84px;width:311px}
.ach .col h3{font-size:15px;font-weight:500;color:var(--brand-red);margin-bottom:8px}
.ach .col .thumb{width:311px;height:120px}
.ach .col p{font-size:10px;line-height:12px;color:#777;margin-top:8px}

/* footer */
.site-footer{left:0;top:3733px;width:1200px;height:89px;background:var(--footer);color:var(--footer-text)}
.footer-brand{position:absolute;left:120px;top:28px;font-size:24px;font-weight:500;color:#8c8c8c}
.footer-contact{position:absolute;left:367px;top:28px}
.footer-contact h4{font-size:15px;font-weight:400;color:#c8c8c8}
.footer-contact p{font-size:10px;margin-top:4px}
.social{position:absolute;left:895px;top:26px;display:flex;align-items:center;gap:8px}
.social h4{font-size:15px;font-weight:400;color:#c8c8c8;margin-right:6px}
.social span{width:22px;height:22px;border-radius:50%;background:#8a8a8a}
.copyright{position:absolute;left:895px;top:60px;font-size:9px}
</style>
</head>
<body>

<header class="abs site-header">
  <div class="abs brand"><span>TrulaPay</span><span class="brand-dot"></span></div>
  <nav class="abs main-nav"><span>Home</span><span>Solutions</span><span>Developers</span><span>Partners</span><span>Company</span><span>Resources</span><span>Blog</span></nav>
  <div class="abs call">Call Us
    <svg width="10" height="14" viewBox="0 0 10 14"><rect x="1" y="0.5" width="8" height="13" rx="1.5" fill="none" stroke="#1a1a9a" stroke-width="1.4"/><circle cx="5" cy="11" r="0.9" fill="#1a1a9a"/></svg>
    <strong>555 014 2290</strong></div>
  <div class="abs btn btn-email"><svg width="12" height="9" viewBox="0 0 12 9"><rect x=".5" y=".5" width="11" height="8" fill="none" stroke="#fff"/><path d="M.5 .5 6 5l5.5-4.5" fill="none" stroke="#fff"/></svg>Email Us</div>
  <div class="abs btn btn-login"><svg width="10" height="10" viewBox="0 0 10 10"><path d="M2 5h6M5 2l3 3-3 3" fill="none" stroke="#fff" stroke-width="1.4"/></svg>Login</div>
</header>

<section class="abs hero" role="img" aria-label="Photo of hands handing over a payment card, tinted blue">
  <h1>MAKING PAYMENT PROCESSING<br>FAST, EASY AND FLEXIBLE</h1>
</section>

<section class="abs feature light" style="top:395px">
  <h2 style="left:120px;top:110px">Recuring Billing</h2>
  <p style="left:120px;top:148px">Accept recurring payments on any schedule you set. Store customer details securely, bill cards and bank accounts automatically, and send receipts without lifting a finger. Every charge is logged for easy reporting, and failed payments retry on their own so your cash flow stays steady and your team stays focused on growth.</p>
  <div class="art" style="left:680px;top:70px;width:300px;height:190px;background:linear-gradient(135deg,#c79a3a,#e9d08a 55%,#8e6a22)" role="img" aria-label="Gold payment card with a padlock resting on it"></div>
</section>

<section class="abs feature grey" style="top:772px">
  <div class="art" style="left:210px;top:70px;width:230px;height:200px;background:linear-gradient(135deg,#9fc3e6,#e8eef5 60%,#b8bcc2)" role="img" aria-label="Laptop with a pointing cursor reaching out of the screen"></div>
  <h2 style="left:600px;top:115px">Virtual Terminal</h2>
  <p style="left:600px;top:152px">Key in card and check payments from any browser with no extra hardware. Our virtual terminal works on any computer, keeps sensitive data off your machines, and gives staff simple screens for sales, refunds and voids so every transaction is handled quickly, accurately and with full records kept safely online.</p>
</section>

<section class="abs feature light" style="top:1152px">
  <h2 style="left:120px;top:120px">Scan Checks</h2>
  <p style="left:120px;top:158px">Turn paper checks into electronic deposits in seconds. Scan each check at your counter, capture the image and account details, and send funds straight to your bank. There are no trips to the branch, fewer errors from manual entry, and faster access to the money your customers have already paid you.</p>
  <div class="art" style="left:655px;top:85px;width:370px;height:170px;background:linear-gradient(90deg,#f4f4f4,#3a3a3a 40%,#1e1e1e 80%,#eaeaea)" role="img" aria-label="Black handheld check scanner"></div>
</section>

<section class="abs feature grey" style="top:1531px">
  <div class="art" style="left:272px;top:68px;width:170px;height:250px;background:linear-gradient(160deg,#7ec84a,#2f9a2e 60%,#1e6f25)" role="img" aria-label="Accounting software product box"></div>
  <h2 style="left:598px;top:115px">Ledgerly Integration</h2>
  <p style="left:598px;top:152px">Connect payments directly to your accounting software. Sales, deposits and fees flow into your books automatically, so reconciliation takes minutes instead of hours. Your records stay current, your accountant gets clean data, and you can see exactly where every dollar stands at the end of each business day and month.</p>
</section>

<section class="abs payform">
  <h2>Website Payment Form</h2>
  <p class="lead">Add a secure hosted payment form to your website in minutes and start accepting cards and bank payments online. Match the form to your brand, choose the fields you need, and let us handle the security so your customers can pay with confidence from any device at any time of day.</p>
  <div class="item" style="left:120px"><div class="thumb" role="img" aria-label="Hand using a calculator on paperwork" style="background:linear-gradient(135deg,#f1e6c8,#c9a24d)"></div><div><h3>Easy Setup</h3><p>Copy a short snippet onto your page and your payment form is live with no coding skills needed.</p></div></div>
  <div class="rule" style="left:436px"></div>
  <div class="item" style="left:460px"><div class="thumb" role="img" aria-label="Hands typing on a keyboard" style="background:linear-gradient(135deg,#e8c3a3,#8a5a3c)"></div><div><h3>Any Device</h3><p>Forms adapt to phones, tablets and desktops so customers can pay wherever they happen to be.</p></div></div>
  <div class="rule" style="left:770px"></div>
  <div class="item" style="left:800px"><div class="thumb" role="img" aria-label="Payment card beside a padlock" style="background:linear-gradient(135deg,#3a3a3a,#d9b640)"></div><div><h3>Safe Checkout</h3><p>Card data is encrypted and stored off your servers, keeping every payment protected end to end.</p></div></div>
</section>

<section class="abs feature grey" style="top:2293px">
  <div class="art" style="left:120px;top:80px;width:400px;height:200px;background:linear-gradient(90deg,#2a2a2a,#a9c9ea 30%,#f1f1f1 50%,#a9c9ea 70%,#2a2a2a)" role="img" aria-label="Two computer monitors with hands passing a card between them"></div>
  <h2 style="left:598px;top:115px">Transaction API</h2>
  <p style="left:598px;top:152px">Build payments into your own software with our developer friendly API. Clear documentation, sandbox testing and client libraries help you ship faster. Process cards and bank transfers, manage customers and pull reports with simple requests, while we take care of compliance, security and the heavy lifting behind every single transaction.</p>
</section>

<section class="abs feature light" style="top:2670px">
  <h2 style="left:120px;top:110px">Electronic Invoicing</h2>
  <p style="left:120px;top:148px">Send professional invoices by email and get paid online in one click. Customers choose card or bank payment, and you see the moment an invoice is viewed and settled. Automatic reminders reduce late payments, and everything ties back to your reports so chasing money becomes a thing of the past.</p>
  <div class="art" style="left:640px;top:95px;width:340px;height:180px;background:linear-gradient(135deg,#e6e6e6,#4a4a4a 50%,#1f1f1f)" role="img" aria-label="Card payment terminal on a clipboard with invoices"></div>
</section>

<section class="abs feature grey" style="top:3050px">
  <div class="art" style="left:175px;top:95px;width:350px;height:170px;background:linear-gradient(135deg,#1f2b3a,#4fb0d6 50%,#9a9a9a)" role="img" aria-label="Smartphone showing a payment card on screen"></div>
  <h2 style="left:598px;top:98px">Mobile</h2>
  <p style="left:598px;top:135px">Take payments anywhere with your phone or tablet. Accept cards in the field, at events or at the customer's door, and send digital receipts instantly. Every mobile sale syncs with your account so your reports stay complete, no matter where the work happens or how many people on your team are selling.</p>
</section>

<section class="abs ach">
  <h2>ACH Payment <span>Processing</span></h2>
  <div class="rule"></div>
  <div class="col" style="left:120px"><h3>Payment Gateway</h3><div class="thumb" role="img" aria-label="Payment card with a chain and padlock" style="background:linear-gradient(135deg,#c9d3de,#5f6b7a)"></div><p>Route every payment through one secure gateway built for speed, uptime and easy reporting.</p></div>
  <div class="col" style="left:446px"><h3>ACH Payment API</h3><div class="thumb" role="img" aria-label="Person using a smartphone at a table" style="background:linear-gradient(135deg,#f0b13a,#c0392b 50%,#3a3a3a)"></div><p>Move money between bank accounts with simple calls and clear status updates at every step.</p></div>
  <div class="col" style="left:772px"><h3>Processing for Software Development</h3><div class="thumb" role="img" aria-label="Hand sketching a light bulb idea on paper" style="background:linear-gradient(135deg,#f4f4f4,#9a9a9a)"></div><p>Give your software built in payments and earn revenue from every transaction your users make.</p></div>
</section>

<footer class="abs site-footer">
  <div class="footer-brand">TrulaPay</div>
  <div class="footer-contact"><h4>Contact Information</h4><p>Reach our support team any weekday for quick help.</p></div>
  <div class="social"><h4>We're SOCIAL</h4><span></span><span></span><span></span></div>
  <div class="copyright">© Copyright TrulaPay. All rights reserved.</div>
</footer>

</body>
</html>
```